Premium CBD/Hemp company needs packaging and label design

Verdant Oakfield, a premium CBD/Hemp company based in Scottsdale, Arizona is in need of a packaging and label design. We are launching with our flagship product which will be a 30 count capsule and will come in three functions: Pain Relief, Anxiety Support, and Sleep Support. For the purpose of this contest, please design packaging and label for our Anxiety Support product. Our products are physician formulated and all natural. Our main ingredient is CBD/Hemp and is complemented by specific herbs that synergistically work together to give the customer the most effective and desired result. We would like our branding to have a pharmaceutical look and feel with a focus on trust and transparency. We have uploaded our company logo that is to be used on both the packaging and label. We have also uploaded an executed branding questionnaire that will guide you to exactly what we are seeking to achieve as to the look and feel of our brand. Please feel free to contact us with any questions that you may have. The winner of this contest will have the opportunity to work with us on future projects as we will need packaging and label design for our entire Verdant Oakfield product line.

Target Market(s)

See attached branding questionnaire

Industry/Entity Type

Health And Wellness

Font styles to use
Sans Serif

Colors

Designer to choose colors to be used in the design.

Requirements
Must have
• See attached branding questionnaire; Please superimpose labels onto a cobalt blue capsule bottle (see attached)
• >>UPON REVIEW of the FIRST 8 designs, we really like the silver, mildly metallic label background in DESIGN # 21300528, we do not want metalic lettering as that would not look very "Pharmaceutical"
• >>We are in search of a look that is a bit more "Pharmaceutical" than a look that would be more commonly found in a Supplement Store
Nice to have
• "See attached branding questionnaire
Should not have
• See attached branding questionnaire; NO marijuana or cannabis plant on the packaging or label

```html
<!DOCTYPE html>
<html lang="en">
<head>
<meta charset="utf-8">
<title>Verdant Oakfield — Anxiety Support Label</title>
<link href="https://fonts.googleapis.com/css2?family=Montserrat:wght@500;600&family=Oswald:wght@600;700&display=swap" rel="stylesheet">
<style>
  :root {
    --backdrop: #e6e7ea;
    --label-white: #ffffff;
    --brand-blue: #2f4aa6;
    --ink-navy: #1f2f7e;
    --rule-blue: #3a4fa8;
    --foliage-deep: #34505c;
    --foliage-mid: #4f6f7a;
    --foliage-violet: #4a4676;
  }
  * { margin: 0; padding: 0; box-sizing: border-box; }
  html, body {
    width: 1200px; height: 960px; overflow: hidden;
    background: var(--backdrop);
  }
  .canvas {
    width: 1200px; height: 960px;
    display: flex; align-items: center; justify-content: center;
  }
  .label {
    width: 700px; height: 860px;
    background: var(--label-white);
    display: flex; flex-direction: column; align-items: center;
    box-shadow: 0 4px 18px rgba(0,0,0,0.08);
  }
  .brand {
    margin-top: 120px;
    display: flex; align-items: center; gap: 22px;
  }
  .brand-dot {
    width: 64px; height: 64px; border-radius: 50%;
    background: var(--brand-blue);
    flex-shrink: 0;
  }
  .brand-name {
    font-family: "Montserrat", sans-serif;
    font-weight: 500;
    font-size: 48px;
    letter-spacing: 1px;
    color: var(--brand-blue);
    white-space: nowrap;
  }
  .product-function {
    margin-top: 110px;
    font-family: "Montserrat", sans-serif;
    font-weight: 600;
    font-size: 48px;
    line-height: 1.1;
    letter-spacing: 1px;
    color: var(--brand-blue);
    white-space: nowrap;
  }
  .product-badge {
    margin-top: 64px;
    position: relative;
    border: 2px solid var(--rule-blue);
    padding: 10px 20px 4px;
  }
  .badge-kicker {
    position: absolute; top: -22px; left: 50%;
    transform: translateX(-50%);
    background: var(--label-white);
    padding: 0 8px;
    font-family: "Montserrat", sans-serif;
    font-weight: 600;
    font-size: 32px;
    line-height: 40px;
    color: var(--brand-blue);
  }
  .badge-title {
    font-family: "Oswald", sans-serif;
    font-weight: 600;
    font-size: 58px;
    line-height: 64px;
    color: var(--ink-navy);
    letter-spacing: 0.5px;
    white-space: nowrap;
  }
  .capsule-count {
    margin-top: 10px;
    font-family: "Oswald", sans-serif;
    font-weight: 600;
    font-size: 34px;
    color: var(--ink-navy);
    display: flex; gap: 22px;
  }
  .capsule-count .count-word {
    letter-spacing: 14px;
    margin-right: -14px;
  }
  .foliage-band {
    margin-top: auto;
    width: 100%; height: 250px;
    background: linear-gradient(120deg, var(--foliage-deep) 0%, var(--foliage-mid) 35%, var(--foliage-violet) 65%, var(--foliage-deep) 100%);
  }
</style>
</head>
<body>
  <main class="canvas">
    <section class="label">
      <div class="brand">
        <span class="brand-dot"></span>
        <span class="brand-name">Verdant Oakfield</span>
      </div>
      <h1 class="product-function">ANXIETY SUPPORT</h1>
      <div class="product-badge">
        <span class="badge-kicker">PREMIUM</span>
        <p class="badge-title">CBD HEMP CAPSULE</p>
      </div>
      <p class="capsule-count"><span class="count-number">30</span><span class="count-word">CAPSULE</span></p>
      <div class="foliage-band" role="img" aria-label="Close-up photograph of dense green and violet leaves"></div>
    </section>
  </main>
</body>
</html>
```